Harwell Properties Business Cards

I would like a business card that includes myself and my partner.
Includes: Logo, office #, email, website, our names, our numbers and possibly the address. I would also like the logo to be embossed and the card to be horizontal.
There is a photo of our yard signs to give you an idea of the colors of our business.

Target Market(s)

Everyone in real estate market.
We are in a rural area. Our clientele are from all socioeconomic backgrounds.

Industry/Entity Type

Real Estate Agent

Contact Information for Business Card

Company Name: Harwell Properties
Our Names, Titles & Cell #'s : Dana Harwell-Broker (555).613.2947, Marla Harwell-Realtor (555).730.5816
Office #: (555).264.1300
Website: harwellproperties.example
Joint Email: harwell@harwellproperties.example
Office Address: 418C W. Pell Creek St.
Fernridge, NV. 00518

Font styles to use
Serif

Requirements
Must have
• HORIZONTAL, Logo, Myself and my partners names, Our cell #'s, our office #, our website, our email address
Nice to have
• Embossed logo, office address, our titles.

```html
<!DOCTYPE html>
<html lang="en">
<head>
<meta charset="utf-8">
<title>Harwell Properties Business Cards</title>
<link rel="stylesheet" href="https://fonts.googleapis.com/css2?family=Open+Sans:wght@400;600;700&display=swap">
<style>
  :root {
    --purple: #4b1f6e;
    --purple-deep: #361352;
    --purple-light: #5d2d85;
    --ink: #3d3d3d;
    --paper: #ffffff;
    --backdrop: #ece9e4;
    --lavender: #cbb6df;
  }
  * { margin: 0; padding: 0; box-sizing: border-box; }
  html, body { width: 1200px; height: 843px; overflow: hidden; }
  body {
    background: var(--backdrop);
    font-family: "Open Sans", Arial, sans-serif;
    display: flex;
    flex-direction: column;
    align-items: center;
    justify-content: center;
    gap: 24px;
  }
  .card {
    width: 680px;
    height: 389px;
    position: relative;
    overflow: hidden;
    box-shadow: 0 6px 18px rgba(0,0,0,0.18);
  }

  /* back */
  .card-back {
    background: linear-gradient(160deg, var(--purple-light) 0%, var(--purple) 45%, var(--purple-deep) 100%);
  }
  .card-back .brand {
    position: absolute;
    left: 0; right: 0; top: 138px;
    display: flex;
    justify-content: center;
    align-items: center;
    gap: 16px;
  }
  .card-back .brand-name { color: var(--paper); }
  .card-back .brand-dot { background: var(--paper); }
  .card-back .website {
    position: absolute;
    left: 0; right: 0; bottom: 34px;
    text-align: center;
    color: var(--lavender);
    font-size: 15px;
    letter-spacing: 5px;
  }

  /* brand block */
  .brand-dot {
    width: 46px; height: 46px;
    border-radius: 50%;
    flex: none;
  }
  .brand-name {
    font-weight: 700;
    font-size: 34px;
    letter-spacing: 1px;
    white-space: nowrap;
  }

  /* front */
  .card-front { background: linear-gradient(135deg, #ffffff 55%, #f1f1f3 100%); }
  .card-front .brand {
    position: absolute;
    left: 150px; top: 46px;
    display: flex;
    align-items: center;
    gap: 14px;
  }
  .card-front .brand-name { color: var(--purple); font-size: 30px; }
  .card-front .brand-dot { background: var(--purple); width: 40px; height: 40px; }
  .office {
    position: absolute;
    left: 40px; top: 150px;
    color: var(--ink);
    font-size: 13.5px;
    line-height: 20px;
  }
  .office .contact-line { display: flex; align-items: center; gap: 8px; }
  .office svg { width: 12px; height: 12px; fill: var(--purple); flex: none; }
  .agents {
    position: absolute;
    right: 40px; top: 190px;
    text-align: right;
    color: var(--ink);
  }
  .agent { margin-bottom: 8px; }
  .agent-name { color: var(--purple); font-weight: 600; font-size: 19px; }
  .agent-title { font-size: 14px; margin-left: 6px; }
  .agent-phone { font-size: 14px; line-height: 18px; }
  .rule {
    position: absolute;
    left: 0; right: 0; top: 300px;
    height: 4px;
    background: var(--purple);
  }
  .band {
    position: absolute;
    left: 0; right: 0; top: 310px;
    height: 50px;
    background: var(--purple);
    color: var(--paper);
    font-size: 16px;
    letter-spacing: 4px;
    display: flex;
    align-items: center;
    padding-left: 40px;
  }
</style>
</head>
<body>

  <section class="card card-back" aria-label="Card back">
    <div class="brand">
      <span class="brand-dot"></span>
      <span class="brand-name">Harwell Properties</span>
    </div>
    <p class="website">www.harwellproperties.example</p>
  </section>

  <section class="card card-front" aria-label="Card front">
    <div class="brand">
      <span class="brand-dot"></span>
      <span class="brand-name">Harwell Properties</span>
    </div>

    <div class="office">
      <p>418C W. Pell Creek St.</p>
      <p>Fernridge, NV. 00518</p>
      <p class="contact-line">
        <svg viewBox="0 0 24 24" aria-hidden="true"><path d="M6.6 10.8a15.2 15.2 0 0 0 6.6 6.6l2.2-2.2c.3-.3.7-.4 1-.2 1.1.4 2.3.6 3.6.6.6 0 1 .4 1 1V20c0 .6-.4 1-1 1A17 17 0 0 1 3 4c0-.6.4-1 1-1h3.5c.6 0 1 .4 1 1 0 1.3.2 2.5.6 3.6.1.3 0 .7-.2 1z"/></svg>
        (555).264.1300
      </p>
      <p class="contact-line">
        <svg viewBox="0 0 24 24" aria-hidden="true"><path d="M2 5h20v14H2z M2 5l10 8 10-8" stroke="#fff" stroke-width="1.5"/></svg>
        harwell@harwellproperties.example
      </p>
    </div>

    <div class="agents">
      <div class="agent">
        <p><span class="agent-name">Dana Harwell,</span><span class="agent-title">Broker</span></p>
        <p class="agent-phone">(555).613.2947</p>
      </div>
      <div class="agent">
        <p><span class="agent-name">Marla Harwell,</span><span class="agent-title">Realtor</span></p>
        <p class="agent-phone">(555).730.5816</p>
      </div>
    </div>

    <div class="rule"></div>
    <div class="band">www.harwellproperties.example</div>
  </section>

</body>
</html>
```